Member Dashboard needs a facelift

Our company is in the consumer credit industry. We offer a service, and once a person signs up for that service, they become a "Member". As a member, they can sign into our "Member Dashboard". What we are looking for is a facelift to our current "Member Dashboard" pages.

We are looking for a cleaner, more modern design that incorporates the same functionality of the current pages (tabs and charts). The graphics elements, buttons and top navigation menu need updating as well.

We are looking for only the page design "look and Feel" and some new great ideas graphicly. Not looking for an entire site.

Please note that the grey background shown in the screen shots is full browser width.

Thank you.
Updates

Thank you everyone for your designs.  Please make sure all designs are in by the end of day.  We will be selecting the 1st and 2nd design tomorrow AM.

 

Thank you for your partisapation.

 

Target Market(s)

Adults over the age of 18 who pay rent in housing.

Industry/Entity Type

Industry

Requirements
Must have
• We are looking for a professional modern look that keeps with the current structure of the current member dashboard. The pages are 1152px wide.

```html
<!DOCTYPE html>
<html lang="en">
<head>
<meta charset="utf-8">
<title>Member Dashboard</title>
<link rel="stylesheet" href="https://fonts.googleapis.com/css2?family=PT+Sans:wght@400;700&display=swap">
<style>
:root{
  --page:#efefef;
  --white:#ffffff;
  --sky:#19b6ee;
  --nav-top:#4fc9f7;
  --nav-bottom:#1573d8;
  --teal:#1aa3d6;
  --title:#1aa0e0;
  --link:#2a8fe0;
  --ink:#222222;
  --muted:#555555;
  --line:#d6d6d6;
  --ribbon:#f6d24a;
  --ribbon-dark:#d9a91c;
  --soft:#f4f4f4;
  --red:#f0605f;
  --green:#7fc48f;
  --pink:#f8a0c4;
  --yellow:#fde07a;
  --blue:#8ed9f0;
  --btn:#1f63c4;
}
*{box-sizing:border-box;margin:0;padding:0}
html,body{width:929px;height:1200px;overflow:hidden}
body{background:var(--page);font-family:"PT Sans",sans-serif;color:var(--ink);position:relative}
.page{position:absolute;left:17px;top:0;width:892px;height:1200px;background:var(--white)}
.abs{position:absolute}

.header{left:0;top:0;width:892px;height:101px;background:linear-gradient(180deg,#1a9fe4 0%,#2fc3f2 100%);border-radius:0 0 4px 4px}
.brand{left:22px;top:22px;font-size:42px;font-weight:700;color:var(--white)}
.account{right:24px;top:10px;color:var(--white);font-size:9px;line-height:18px}
.account b{font-weight:700}
.account .meta{font-size:7px;line-height:9px;margin-top:4px}

.nav{left:0;top:101px;width:892px;height:93px;background:linear-gradient(180deg,var(--nav-top) 0%,#2b98e8 45%,var(--nav-bottom) 100%);border-radius:0 0 8px 8px;overflow:hidden}
.nav-item{position:absolute;top:0;height:93px;text-align:center;color:var(--white);font-weight:700;font-size:18px;border-right:1px solid rgba(255,255,255,.25)}
.nav-item.active{background:rgba(255,255,255,.12)}
.nav-icon{display:block;margin:8px auto 4px;width:60px;height:50px;border-radius:8px}

.landlord{left:9px;top:214px;width:511px;height:373px;border:1px solid var(--line);border-radius:8px;overflow:hidden;background:var(--white)}
.tabband{left:0;top:0;width:511px;height:67px;background:linear-gradient(180deg,#0f95c8,#2fb7e2)}
.ribbon{position:absolute;top:-4px;width:64px;height:72px;background:var(--ribbon);clip-path:polygon(0 0,100% 0,100% 100%,50% 86%,0 100%);text-align:center;font-size:11px;line-height:15px;color:var(--teal);padding-top:18px;border-left:2px solid var(--ribbon-dark);border-right:2px solid var(--ribbon-dark)}
.ribbon.current{background:#4fc2e3;color:#123;border-color:#2a9ac4}
.lv-title{left:12px;top:80px;font-size:27px;line-height:30px;color:var(--title);font-weight:400;white-space:nowrap}
.form-label{position:absolute;left:14px;font-size:10px;line-height:16px}
.form-input{position:absolute;left:112px;width:190px;height:16px;border:1px solid #cfcfcf;background:#fafafa}
.apply{left:12px;top:330px;width:72px;height:23px;background:var(--btn);color:var(--white);font-size:11px;font-weight:700;line-height:23px;padding-left:9px;clip-path:polygon(0 0,90% 0,100% 50%,90% 100%,0 100%);border-radius:3px 0 0 3px}
.info{position:absolute;left:341px;width:165px;background:var(--soft);padding:5px 6px}
.info h3{font-size:13px;font-weight:400;line-height:16px;margin-bottom:5px}
.info p{font-size:8px;line-height:11px;color:var(--muted)}

.mvc-title{left:543px;top:222px;width:340px;text-align:center;font-size:19px}
.gauge{position:absolute;width:170px;text-align:center}
.gauge svg{display:block;margin:0 auto}
.gauge .ends{display:flex;justify-content:space-between;padding:0 14px;font-size:10px;font-weight:700;margin-top:-6px}
.gauge .cap{font-size:11.5px;color:var(--title);margin-top:2px;white-space:nowrap}

.factors{left:4px;top:607px;width:886px;height:115px;border:1px solid var(--line);border-radius:6px;background:linear-gradient(180deg,#fff,#f3f3f3)}
.factor{position:absolute;top:0;height:113px;border-right:1px solid var(--line);padding:12px 14px}
.factor h4{font-size:18px;font-weight:700;display:flex;align-items:center;gap:4px;white-space:nowrap}
.factor p{font-size:9px;line-height:11px;color:var(--muted);margin-top:14px;letter-spacing:.2px}
.factor a{display:block;text-align:right;font-size:11px;color:var(--link);text-decoration:none;margin-top:8px}
.continue{left:731px;top:614px;width:164px;height:98px;background:var(--sky);clip-path:polygon(4% 6%,100% 0,96% 100%,0 94%);color:var(--white);font-size:23px;font-weight:700;line-height:22px;padding:20px 0 0 22px}
.curl{left:703px;top:612px;width:40px;height:132px;background:linear-gradient(90deg,#cfcfcf,#ffffff 60%,#e4e4e4);clip-path:polygon(60% 0,100% 4%,90% 100%,30% 96%,0 60%)}

.factors-title{left:36px;top:736px;font-size:22px;font-weight:700}
.factors-text{left:38px;top:764px;width:500px;font-size:12px;line-height:19px}
.donut{left:30px;top:805px}
.donut-label{position:absolute;font-size:17px;line-height:15px;font-weight:700;color:#333}

.legend{left:545px;top:804px;width:330px}
.legend h3{font-size:15px;font-weight:700;margin-bottom:14px}
.legend .intro{font-size:9.5px;line-height:19px;margin-bottom:9px}
.legend-item{height:47px}
.legend-item h5{font-size:9.5px;font-weight:700;display:flex;align-items:center;gap:9px}
.legend-item h5 i{width:12px;height:12px;border:1px solid rgba(0,0,0,.15)}
.legend-item p{font-size:8.5px;line-height:11px;color:var(--muted);margin-top:4px}

.footer{left:0;top:1148px;width:892px;border-top:2px solid #cccccc;text-align:center;padding-top:20px;font-size:11px}
.footer span{color:#7fd4f0}
</style>
</head>
<body>
<div class="page">

  <header class="header abs">
    <div class="brand abs">Logo Here</div>
    <div class="account abs">
      <div>Welcome <b>Administrator</b></div>
      <div>⚙ My Account | Log out</div>
      <div>✉ 4 new messages</div>
      <div class="meta">Server time : 6:45 AM<br>Last login ip : 192.168.0.15</div>
    </div>
  </header>

  <nav class="nav abs">
    <div class="nav-item active" style="left:0;width:180px">
      <span class="nav-icon" role="img" aria-label="House illustration" style="background:linear-gradient(#c99a5a,#8a6a3a)"></span>Member Home</div>
    <div class="nav-item" style="left:180px;width:201px">
      <span class="nav-icon" role="img" aria-label="Group of members illustration" style="background:linear-gradient(#6a7fa8,#2d3b5a)"></span>Rent Profile</div>
    <div class="nav-item" style="left:381px;width:221px">
      <span class="nav-icon" role="img" aria-label="Pie chart illustration" style="background:linear-gradient(#fdd34c,#f0605f)"></span>Credit Summary</div>
    <div class="nav-item" style="left:602px;width:290px;border-right:none">
      <span class="nav-icon" role="img" aria-label="Question mark illustration" style="width:36px;background:linear-gradient(#d04cc0,#f3c028)"></span>Frequently Asked Questions</div>
  </nav>

  <section class="landlord abs">
    <div class="tabband abs">
      <div class="ribbon" style="left:40px">Member<br>Name</div>
      <div class="ribbon" style="left:161px">Rental<br>Address</div>
      <div class="ribbon" style="left:285px">Member<br>Contact</div>
      <div class="ribbon current" style="left:407px">Landlord<br>Contact</div>
    </div>
    <h2 class="lv-title abs">Landlord Verification Center</h2>
    <label class="form-label" style="top:120px">Name :</label><span class="form-input" style="top:120px"></span>
    <label class="form-label" style="top:151px">Management :</label><span class="form-input" style="top:151px"></span>
    <label class="form-label" style="top:182px">City</label><span class="form-input" style="top:182px"></span>
    <label class="form-label" style="top:213px">Street Address :</label><span class="form-input" style="top:213px"></span>
    <label class="form-label" style="top:244px">Street Address 2 :</label><span class="form-input" style="top:244px"></span>
    <label class="form-label" style="top:275px">Zip Code :</label><span class="form-input" style="top:275px"></span>
    <label class="form-label" style="top:306px">Email :</label><span class="form-input" style="top:306px"></span>
    <div class="apply abs">Apply/Edit</div>
    <div class="info" style="top:112px">
      <h3>Why You Want<br>Landlord Verification ?</h3>
      <p>Lorem ipsum dolor sit amet, consectetur adipiscing elit. Etiam vitae urna eu felis mollis hendrerit non nec mi. Pellentesque nec velit non velit tincidunt lobortis ac sed elit. Donec sed velit nulla, vel elementum mi.</p>
    </div>
    <div class="info" style="top:237px">
      <h3>What is<br>Landlord Verification ?</h3>
      <p>Lorem ipsum dolor sit amet, consectetur adipiscing elit. Etiam vitae urna eu felis mollis hendrerit non nec mi. Pellentesque nec velit non velit tincidunt lobortis ac sed elit. Donec sed velit nulla, vel elementum mi.</p>
    </div>
  </section>

  <h2 class="mvc-title abs">Member Verification Center</h2>
  <svg width="0" height="0" style="position:absolute">
    <defs>
      <linearGradient id="arc" x1="0" y1="1" x2="1" y2="0">
        <stop offset="0" stop-color="#e0302a"/><stop offset=".55" stop-color="#f2a23a"/><stop offset="1" stop-color="#7fd83a"/>
      </linearGradient>
      <symbol id="dial" viewBox="0 0 100 100">
        <circle cx="50" cy="50" r="48" fill="#d8d8d8"/>
        <circle cx="50" cy="50" r="45" fill="#1b1b1b"/>
        <path d="M18 72 A38 38 0 1 1 82 72" fill="none" stroke="url(#arc)" stroke-width="6"/>
        <polygon points="48,22 52,22 54,65 50,68 46,65" fill="#f2d98a" transform="rotate(-12 50 50)"/>
      </symbol>
    </defs>
  </svg>
  <div class="gauge" style="left:526px;top:279px"><svg width="94" height="94"><use href="#dial"/></svg><div class="ends"><span>Attention</span><span>Verified</span></div><div class="cap">Member Contact Verification</div></div>
  <div class="gauge" style="left:716px;top:279px"><svg width="94" height="94"><use href="#dial"/></svg><div class="ends"><span>Attention</span><span>Verified</span></div><div class="cap">Member Contact Verification</div></div>
  <div class="gauge" style="left:526px;top:413px"><svg width="94" height="94"><use href="#dial"/></svg><div class="ends"><span>Attention</span><span>Verified</span></div><div class="cap">Member Contact Verification</div></div>
  <div class="gauge" style="left:716px;top:413px"><svg width="94" height="94" style="filter:drop-shadow(0 0 8px #35c8f5)"><use href="#dial"/></svg><div class="ends"><span>Attention</span><span>Verified</span></div><div class="cap">Member Contact Verification</div></div>

  <section class="factors abs">
    <div class="factor" style="left:0;width:144px"><h4><svg width="28" height="28" viewBox="0 0 28 28"><circle cx="14" cy="14" r="11" fill="none" stroke="#1a8fe0" stroke-width="3"/><path d="M14 8v7l5 3" stroke="#1a8fe0" stroke-width="2.5" fill="none"/></svg>History</h4><p>Maecenas non nisi nec interdum mattis. Fusce acpurus.</p><a>More Info &gt;&gt;</a></div>
    <div class="factor" style="left:144px;width:143px"><h4><svg width="32" height="26" viewBox="0 0 32 26"><path d="M16 2v22M6 6h20M6 6l-5 10h10zM26 6l-5 10h10zM10 24h12" stroke="#1a8fe0" stroke-width="2" fill="none"/></svg>Balances</h4><p>Maecenas non nisi nec interdum mattis. Fusce acpurus.</p><a>More Info &gt;&gt;</a></div>
    <div class="factor" style="left:287px;width:132px"><h4><svg width="24" height="26" viewBox="0 0 24 26"><rect x="2" y="2" width="20" height="20" rx="3" fill="none" stroke="#1a8fe0" stroke-width="2.5"/><path d="M7 15l6-7 2 6" stroke="#1a8fe0" stroke-width="2" fill="none"/></svg>Acct. Age</h4><p>Maecenas non nisi nec interdum mattis. Fusce acpurus.</p><a>More Info &gt;&gt;</a></div>
    <div class="factor" style="left:419px;width:158px"><h4><svg width="34" height="24" viewBox="0 0 34 24"><rect x="1" y="5" width="28" height="17" rx="2" fill="#1a8fe0"/><rect x="6" y="1" width="27" height="16" rx="2" fill="#6cc8f5"/></svg>New Credit</h4><p>Maecenas non nisi nec interdum mattis. Fusce acpurus.</p><a>More Info &gt;&gt;</a></div>
    <div class="factor" style="left:577px;width:130px;border-right:none"><h4><svg width="30" height="26" viewBox="0 0 30 26"><rect x="1" y="2" width="13" height="24" fill="#1a8fe0"/><rect x="16" y="8" width="13" height="18" fill="#1a8fe0"/><path d="M4 6h3M9 6h2M4 11h3M9 11h2M4 16h3M9 16h2M19 12h3M24 12h2M19 17h3M24 17h2" stroke="#fff" stroke-width="2"/></svg>Types</h4><p>Maecenas non nisi nec interdum mattis. Fusce acpurus.</p><a>More Info &gt;&gt;</a></div>
  </section>
  <div class="curl abs"></div>
  <div class="continue abs">Continue To<br>Your Rent<br>Profile</div>

  <h2 class="factors-title abs">The 5 Factors That Determine Your Credit Score :</h2>
  <p class="factors-text abs">Lorem ipsum dolor sit amet, consectetur adipiscing elit. Etiam vitae urna eu felis mollis non nec mi. Pellentesque nec velit non velit tincidunt lobortis ac sed elit.</p>

  <svg class="donut abs" width="320" height="320" viewBox="0 0 320 320" role="img" aria-label="Credit score factor breakdown chart">
    <g fill="none" stroke-width="38" transform="translate(178 161)">
      <path d="M0 -96 A96 96 0 0 1 60 -75" stroke="var(--red)"/>
      <path d="M63 -72 A96 96 0 0 1 96 0" stroke="var(--green)"/>
      <path d="M96 4 A96 96 0 0 1 52 81" stroke="var(--pink)"/>
      <path d="M48 83 A96 96 0 0 1 -88 38" stroke="var(--yellow)"/>
      <path d="M-90 33 A96 96 0 0 1 -4 -96" stroke="var(--blue)"/>
    </g>
    <g font-family="PT Sans, sans-serif" font-size="19" fill="#fff" font-weight="700" text-anchor="middle" dominant-baseline="central">
      <text x="211" y="71" transform="rotate(20 211 71)">10%</text>
      <text x="265" y="120" transform="rotate(65 265 120)">20%</text>
      <text x="261" y="209" transform="rotate(-60 261 209)">30%</text>
      <text x="145" y="251" transform="rotate(20 145 251)">40%</text>
      <text x="99" y="106" transform="rotate(-55 99 106)">50%</text>
    </g>
  </svg>
  <div class="donut-label" style="left:236px;top:813px">Payment<br>History</div>
  <div class="donut-label" style="left:319px;top:886px">Payment<br>History</div>
  <div class="donut-label" style="left:324px;top:1012px">Payment<br>History</div>
  <div class="donut-label" style="left:115px;top:1078px">Payment<br>History</div>
  <div class="donut-label" style="left:33px;top:875px">Payment<br>History</div>

  <aside class="legend abs">
    <h3>Credit History.</h3>
    <p class="intro">A breakdown of History and<br>the amount of time spent on each... roughly.</p>
    <div class="legend-item"><h5><i style="background:var(--blue)"></i>Payment History 50%</h5><p>Maecenas non nisi nec lacus interdum mattis. Fusce ac mi purus. lobortis turpis accumsan vitae. Nam pulvinar congue ante, viverra</p></div>
    <div class="legend-item"><h5><i style="background:var(--yellow)"></i>Payment History 50%</h5><p>Maecenas non nisi nec lacus interdum mattis. Fusce ac mi purus. lobortis turpis accumsan vitae. Nam pulvinar congue ante, viverra</p></div>
    <div class="legend-item"><h5><i style="background:var(--pink)"></i>Payment History 50%</h5><p>Maecenas non nisi nec lacus interdum mattis. Fusce ac mi purus. lobortis turpis accumsan vitae. Nam pulvinar congue ante, viverra</p></div>
    <div class="legend-item"><h5><i style="background:var(--green)"></i>Payment History 50%</h5><p>Maecenas non nisi nec lacus interdum mattis. Fusce ac mi purus. lobortis turpis accumsan vitae. Nam pulvinar congue ante, viverra</p></div>
    <div class="legend-item"><h5><i style="background:var(--red)"></i>Payment History 50%</h5><p>Maecenas non nisi nec lacus interdum mattis. Fusce ac mi purus. lobortis turpis accumsan vitae. Nam pulvinar congue ante, viverra</p></div>
  </aside>

  <footer class="footer abs">Copyright 2012 - <span>Logo here</span> &nbsp;All Rights Reserved</footer>
</div>
</body>
</html>
```